Financial advisory firm needs new business card design

Business card design , simple , elegant, professional. Will use existing logo. One side should be a solid blue background (matching blue in Logo) . info side should have basic info, maybe two color panes. one white, one a different color..maybe light grey. Please visit our website to get feel for colors and business. www.tallowmeadwealth.com

Industry/Entity Type

Financial Service

Contact Information for Business Card

Basic info..minimalist, modern, approach

Colors

Designer to choose colors to be used in the design.

Requirements
Must have
• Important regulatory requirement. The following disclosure MUST be included somewhere on the business card. It can be either front, or back, and it may be in a smaller font (but has to be legible). My interest is to satisfy the requirement with the least possible disruption to the beauty of the card design.
• All securities offered through the Harrowgate Capital, Inc. Oakhurst Lane, NJ. Member QOLTA/DWEM. Advisory services provided through HC Advisory Services, Inc. an PBR Registered Investment Advisor.

```html
<!DOCTYPE html>
<html lang="en">
<head>
<meta charset="utf-8">
<title>Tallowmead Wealth — Business Card</title>
<link href="https://fonts.googleapis.com/css2?family=Roboto+Condensed:wght@400;700&display=swap" rel="stylesheet">
<style>
  :root {
    --bg: #d9dadc;
    --brand-blue: #1a7dc6;
    --brand-blue-deep: #0f6fb7;
    --ink: #141414;
    --muted: #555a60;
    --navy: #123a78;
    --accent: #1f6fc0;
    --card-white: #ffffff;
  }
  * { margin: 0; padding: 0; box-sizing: border-box; }
  html, body { width: 1200px; height: 1200px; overflow: hidden; }
  body {
    background: var(--bg);
    font-family: "Roboto Condensed", "Arial Narrow", sans-serif;
    position: relative;
  }
  .card {
    position: absolute;
    left: 150px;
    width: 900px;
    height: 514px;
    border-radius: 34px;
    overflow: hidden;
    box-shadow: 0 10px 28px rgba(0,0,0,0.18);
  }
  .card--front {
    top: 62px;
    background: linear-gradient(180deg, var(--brand-blue) 0%, var(--brand-blue-deep) 100%);
    display: flex;
    align-items: center;
    justify-content: center;
  }
  .card--back {
    top: 624px;
    background: var(--card-white);
  }
  .brand {
    display: flex;
    align-items: center;
    gap: 16px;
    font-weight: 700;
    text-transform: uppercase;
    letter-spacing: 3px;
    white-space: nowrap;
  }
  .brand__dot {
    border-radius: 50%;
    flex: none;
  }
  .card--front .brand { color: var(--ink); font-size: 58px; }
  .card--front .brand__dot { width: 30px; height: 30px; background: var(--ink); }
  .card--back .brand {
    position: absolute;
    left: 90px;
    top: 236px;
    color: var(--ink);
    font-size: 34px;
    gap: 10px;
  }
  .card--back .brand__dot { width: 18px; height: 18px; background: var(--ink); }
  .rule {
    position: absolute;
    height: 3px;
    background: var(--accent);
  }
  .rule--left { left: 0; top: 256px; width: 72px; }
  .rule--right { left: 504px; top: 256px; width: 346px; }
  .identity {
    position: absolute;
    right: 50px;
    top: 150px;
    text-align: right;
  }
  .identity__name {
    color: var(--navy);
    font-weight: 700;
    font-size: 46px;
    line-height: 1;
    letter-spacing: 0.5px;
  }
  .identity__role {
    color: var(--accent);
    font-size: 26px;
    line-height: 1.1;
    letter-spacing: 1px;
  }
  .contact {
    position: absolute;
    right: 50px;
    top: 280px;
    text-align: right;
    color: var(--ink);
    font-size: 25px;
    line-height: 1.32;
    list-style: none;
  }
  .contact__gap { margin-top: 14px; }
  .disclosure {
    position: absolute;
    left: 50px;
    bottom: 40px;
    width: 400px;
    color: var(--muted);
    font-size: 15px;
    line-height: 1.35;
  }
</style>
</head>
<body>
  <section class="card card--front" aria-label="Card front">
    <div class="brand">
      <span class="brand__dot"></span>
      <span class="brand__name">Tallowmead Wealth</span>
    </div>
  </section>

  <section class="card card--back" aria-label="Card back">
    <div class="rule rule--left"></div>
    <div class="brand">
      <span class="brand__dot"></span>
      <span class="brand__name">Tallowmead Wealth</span>
    </div>
    <div class="rule rule--right"></div>

    <div class="identity">
      <p class="identity__name">YOUR NAME</p>
      <p class="identity__role">JOB POSITION</p>
    </div>

    <ul class="contact">
      <li>48 Quarry Bend Road, Suite 110</li>
      <li>Linwood Falls, NJ 07415</li>
      <li class="contact__gap">(555) 014-2286</li>
      <li class="contact__gap">info@tallowmeadwealth.com</li>
      <li>www.tallowmeadwealth.com</li>
    </ul>

    <p class="disclosure">All securities offered through Harrowgate Capital, Inc. Oakhurst Lane, NJ. Member QOLTA/DWEM. Advisory services provided through HC Advisory Services, Inc. an PBR Registered Investment Advisor.</p>
  </section>
</body>
</html>
```